Minds At Market Banner

We require a banner ad for a new Facebook group. Group name is 'Minds at Market'.

The group is being put together for the purpose of getting like minded people that either operate or have an interest is business together to discuss and share their challenges, learning’s, results and so that people can share and learn from each other surrounding the topic of business.

The group is also about solutions and strategies for understanding people at a deeper level in the context of business,

The group will be built for people who share four key principles in business:

1. Integrity – We always operate from a place of high integrity.
2. Experience – We strive to create a positive experience and atmosphere for all
3. Respect – We treat people with the utmost of respect
4. Solutions & Actions – We are solution and action orientated

So we require a creative clean simple design for a banner that denotes the group’s purpose and that will become a recognizable symbol that represents the interests of the group.

UPDATE: Banner Ad size is to suite Facebook header and needs to be 851px X 315px.

Update #2 - So it turns out that headers for group pages on Facebook is 800px X 250px and does not have the small square 180px X 180px box on LHS as per a Facebook
pages.

Target Market(s)

Business people and people with an interest in business

Industry/Entity Type

Business

Font styles to use
Sans Serif

Requirements
Must have
• clean and simple
Should not have
• Should not be too busy

```html
<!DOCTYPE html>
<html lang="en">
<head>
<meta charset="utf-8">
<title>Minds at Market Banner</title>
<link href="https://fonts.googleapis.com/css2?family=Josefin+Sans:wght@100;200;300&display=swap" rel="stylesheet">
<style>
  :root {
    --stage-top: #0a0a0a;
    --stage-mid: #4a4445;
    --stage-bottom: #aaa2a2;
    --banner-light: #2ed8e2;
    --banner-mid: #22b4bf;
    --banner-dark: #137a80;
    --ink-dark: #0b3d42;
    --ink-light: #ffffff;
    --crowd-light: #1f8f98;
    --crowd-dark: #0c4d53;
  }
  html, body {
    margin: 0;
    padding: 0;
    width: 1200px;
    height: 1000px;
    overflow: hidden;
  }
  .stage {
    position: relative;
    width: 1200px;
    height: 1000px;
    background: linear-gradient(180deg, var(--stage-top) 0%, var(--stage-mid) 32%, var(--stage-bottom) 70%, var(--stage-bottom) 100%);
    font-family: "Josefin Sans", sans-serif;
  }
  .banner {
    position: absolute;
    left: 64px;
    top: 302px;
    width: 1087px;
    height: 338px;
    overflow: hidden;
    background: linear-gradient(100deg, var(--banner-light) 0%, var(--banner-light) 40%, var(--banner-mid) 70%, var(--banner-dark) 100%);
  }
  .crowd-photo {
    position: absolute;
    left: 236px;
    top: 0;
    width: 815px;
    height: 212px;
    background: linear-gradient(180deg, var(--crowd-dark) 0%, var(--crowd-light) 100%);
    opacity: 0.55;
  }
  .brand-mark {
    position: absolute;
    left: 33px;
    top: 28px;
    width: 143px;
    height: 143px;
    background: var(--banner-light);
    box-shadow: 0 0 22px rgba(8, 70, 76, 0.55);
    display: flex;
    flex-direction: column;
    justify-content: center;
    align-items: center;
    color: var(--ink-light);
    font-weight: 300;
    font-size: 17px;
    line-height: 1.25;
    letter-spacing: 1px;
    text-align: center;
  }
  .title-main {
    position: absolute;
    left: 30px;
    top: 196px;
    margin: 0;
    color: var(--ink-dark);
    font-weight: 100;
    font-size: 134px;
    line-height: 1;
    letter-spacing: 4px;
  }
  .title-joiner {
    position: absolute;
    left: 573px;
    top: 212px;
    color: var(--ink-light);
    font-weight: 200;
    font-size: 34px;
    line-height: 1;
  }
  .title-second {
    position: absolute;
    left: 570px;
    top: 241px;
    color: var(--ink-light);
    font-weight: 100;
    font-size: 90px;
    line-height: 1;
    letter-spacing: 3px;
  }
</style>
</head>
<body>
  <main class="stage">
    <section class="banner">
      <div class="crowd-photo" role="img" aria-label="Row of business people in suits standing side by side, shown from the waist down, tinted teal"></div>
      <div class="brand-mark">
        <span>Minds</span>
        <span>at Market</span>
      </div>
      <h1 class="title-main">MINDS</h1>
      <span class="title-joiner">at</span>
      <span class="title-second">MARKET</span>
    </section>
  </main>
</body>
</html>
```